Commercial and Residential landscape Flyer design

we would like a flyer to advertise our new landscaping division for our company. Phone Number 5184620371
email pinecrestgroundworkservices@mailorbit.net
address 7 Marlow Court Schenectady New York 12419
The design is up to you. ill attach some sample flyers in the file section
Target Market(s)
Residential and commercial properties
Industry/Entity Type
Landscape
Font styles to use
Sans Serif
Colors
Designer to choose colors to be used in the design.
Requirements
Must have
- Services offered
- Spring Cleanups
- Mulch installation
- Mowing
- Tree and shrub Maintenance
- Fall Cleanups
- Fully Insured
- Free Estimates
Nice to have
- See word file Please double check all grammar and spelling
- Feel free to use anything in the word file. Its totally up to you. It all doesn't need to be on it . would like to stick with the color scheme of the logo
Should not have
- there are no should not haves. We just want to get the word out that we have a landscape division

```html
<!DOCTYPE html>
<html lang="en">
<head>
<meta charset="utf-8">
<title>Pinecrest Groundwork Services – Landscaping Flyer</title>
<link rel="stylesheet" href="https://fonts.googleapis.com/css2?family=Questrial&display=swap">
<style>
:root{
  --lawn-deep:#3f7a1e;
  --band:#5e9a2e;
  --panel:#3e5b12;
  --pill:#3b5a14;
  --accent-line:#8cc63f;
  --yellow:#f2ef2a;
  --white:#ffffff;
  --ink:#333333;
  --body:#444444;
  --logo-blue:#1e88e0;
}
*{margin:0;padding:0;box-sizing:border-box}
html,body{width:849px;height:1200px;overflow:hidden;background:var(--white)}
.flyer{position:relative;width:849px;height:1200px;overflow:hidden;font-family:"Questrial",sans-serif;color:var(--ink)}
.shapes{position:absolute;inset:0}
.brand{position:absolute;left:13px;top:58px;width:176px;height:176px;border-radius:50%;background:var(--white);border:5px solid var(--logo-blue);display:flex;align-items:center;justify-content:center;text-align:center;padding:20px;font-size:20px;line-height:1.15;color:var(--logo-blue)}
.headline{position:absolute;left:180px;top:98px;width:560px;text-align:center;font-weight:400;font-size:39px;line-height:44px;color:var(--white);text-shadow:1px 2px 3px rgba(0,0,0,.45)}
.address{position:absolute;left:215px;top:252px;width:430px;text-align:center;font-size:26px;line-height:31px;color:var(--white);text-shadow:1px 2px 3px rgba(0,0,0,.45)}
.pill{position:absolute;left:0;width:346px;height:28px;background:var(--pill);border-radius:0 14px 14px 0;color:var(--white);font-weight:400;font-size:18px;line-height:28px;padding-left:22px}
.pill--intro{top:383px}
.pill--services{top:561px}
.intro{position:absolute;left:29px;top:425px;width:325px;font-size:10.6px;line-height:13px;color:var(--body)}
.intro p+p{margin-top:11px}
.services{list-style:none;position:absolute;left:0;top:604px;font-size:18px;line-height:22px;color:#222}
.services li{position:absolute;white-space:nowrap}
.services li::before{content:"";position:absolute;left:-20px;top:8px;width:7px;height:7px;border-radius:50%;background:var(--lawn-deep)}
.services .s1{left:46px;top:0}
.services .s2{left:82px;top:32px}
.services .s3{left:298px;top:96px}
.services .s4{left:330px;top:134px}
.cta{position:absolute;left:458px;top:838px;width:391px;text-align:center;color:var(--yellow)}
.cta__line{font-size:38px;line-height:42px}
.cta__phone{font-size:38px;line-height:44px;margin-top:8px}
.cta__insured{font-size:16px;line-height:20px;color:var(--white);margin-top:4px}
.cta__email{font-size:13px;line-height:18px;color:var(--white);margin-top:6px}
</style>
</head>
<body>
<div class="flyer">
  <svg class="shapes" width="849" height="1200" viewBox="0 0 849 1200">
    <defs>
      <linearGradient id="heroFill" x1="0" y1="0" x2="0" y2="1">
        <stop offset="0" stop-color="#bcd6e6"/>
        <stop offset=".35" stop-color="#7fae58"/>
        <stop offset="1" stop-color="#4f8a26"/>
      </linearGradient>
      <linearGradient id="mowerFill" x1="0" y1="0" x2="1" y2="1">
        <stop offset="0" stop-color="#7cb342"/>
        <stop offset=".55" stop-color="#e9782a"/>
        <stop offset="1" stop-color="#4e8a23"/>
      </linearGradient>
      <linearGradient id="houseFill" x1="0" y1="0" x2="0" y2="1">
        <stop offset="0" stop-color="#9a8f84"/>
        <stop offset=".5" stop-color="#6d9a3c"/>
        <stop offset="1" stop-color="#b5a894"/>
      </linearGradient>
      <linearGradient id="bedFill" x1="0" y1="0" x2="0" y2="1">
        <stop offset="0" stop-color="#a9adb1"/>
        <stop offset=".5" stop-color="#6e8f3a"/>
        <stop offset="1" stop-color="#5d9a2f"/>
      </linearGradient>
      <linearGradient id="barrowFill" x1="0" y1="0" x2="0" y2="1">
        <stop offset="0" stop-color="#c9cbc7"/>
        <stop offset=".45" stop-color="#b33a2e"/>
        <stop offset=".6" stop-color="#63a233"/>
        <stop offset="1" stop-color="#4f8f24"/>
      </linearGradient>
      <linearGradient id="lawnBottom" x1="0" y1="0" x2="0" y2="1">
        <stop offset="0" stop-color="#8bbf5a"/>
        <stop offset="1" stop-color="#5f9a30"/>
      </linearGradient>
    </defs>

    <rect x="0" y="0" width="849" height="360" fill="url(#heroFill)" role="img" aria-label="Photo of a landscaped commercial lawn with a flower bed"/>
    <rect x="0" y="356" width="849" height="8" fill="var(--accent-line)"/>
    <path d="M155 68 H790 a30 30 0 0 1 30 30 V198 a30 30 0 0 1 -30 30 H155 Z" fill="var(--band)" opacity=".88"/>

    <rect x="0" y="364" width="849" height="836" fill="#ffffff"/>
    <rect x="0" y="1100" width="849" height="100" fill="url(#lawnBottom)" role="img" aria-label="Photo of freshly cut lawn"/>

    <rect x="455" y="810" width="394" height="302" fill="var(--panel)"/>

    <g stroke="#ffffff" stroke-width="6">
      <rect x="585" y="200" width="320" height="320" rx="30" transform="rotate(45 745 360)" fill="url(#mowerFill)" role="img" aria-label="Photo of an orange ride-on lawn mower on a green lawn"/>
      <rect x="580" y="562" width="220" height="220" rx="26" transform="rotate(45 690 672)" fill="url(#bedFill)" role="img" aria-label="Photo of a mulched garden bed edged with stones beside a house"/>
      <rect x="414" y="423" width="204" height="204" rx="24" transform="rotate(45 516 525)" fill="url(#houseFill)" role="img" aria-label="Photo of a landscaped house front with flower beds and stone walkway"/>
      <rect x="69" y="764" width="332" height="332" rx="34" transform="rotate(45 235 930)" fill="url(#barrowFill)" role="img" aria-label="Photo of a red wheelbarrow and shovel on a lawn"/>
    </g>
  </svg>

  <div class="brand">Pinecrest Groundwork Services</div>

  <h1 class="headline">Commercial and Residential Landscaping</h1>
  <p class="address">7 Marlow Court Schenectady<br>New York 12419</p>

  <h2 class="pill pill--intro">Beautify Your Yard or Business</h2>
  <div class="intro">
    <p>We can help you with all phases of the landscaping process, from designing an interesting cohesive layout to installation. In addition to planting trees, shrubs, and flowers, our services also include the design and installation of the following landscaping features: Gardens, including Terraced Gardens, Patios, Walkways, Retaining Walls, and Xeriscaping.</p>
    <p>In addition, we provide mowing, seeding and sodding, mulch installation, rock beds, and spring and fall cleanups.</p>
  </div>

  <h2 class="pill pill--services">Our Service Specialties</h2>
  <ul class="services">
    <li class="s1">Tree and shrub maintenance and removal</li>
    <li class="s2">Tree trimming<br>(hazardous limb removal and view cutting)</li>
    <li class="s3">Single tree removal</li>
    <li class="s4">Installation of new trees,<br>shrubs, perennials, and annuals</li>
  </ul>

  <div class="cta">
    <p class="cta__line">Contact us today<br>for your free,<br>no obligation<br>estimate!</p>
    <p class="cta__phone">518-462-0371</p>
    <p class="cta__insured">Fully Insured · Free Estimates</p>
    <p class="cta__email">pinecrestgroundworkservices@mailorbit.net</p>
  </div>
</div>
</body>
</html>
```